4D Little Lumen Luxury Ultrasound Billboard

Design a HIGH-END, MODERN billboard for my private prenatal ultrasound studio, 4D Little Lumen, located in Pace, Florida.
This billboard will be viewed by drivers traveling at highway speeds, so it must be extremely clean, simple, and readable within 6 seconds.
About My Business
4D Little Lumen is a private prenatal ultrasound studio specializing in:
Highest technology 4D/HD Ultrasounds
Early Gender Determination
Pregnancy Confirmation
I have been serving families for nearly 10 years and is known for creating a memorable experience, not just an ultrasound appointment.
Design Style
I DO NOT want:
Flowers
Leaves
Swirls
Glitter
Hearts everywhere
Busy backgrounds
Generic maternity stock graphics
I DO want:
Modern
Luxury
Upscale
Clean
Professional
Eye-catching
Premium medical spa feel
Colors
Use colors from my logo:
LOGO Green ( or a deep green)
Black
White
Soft Gold accents
Images:
Incorporate my professional headshot in a clean, modern way, logo, and the ultrasound images
Text
Keep wording minimal.
Primary Headline ( OPEN TO IDEAS) :
EXAMPLES ( WOULD RATHER SOMETHING MORE CATCHY)
" ADVANCED IMAGING. UNFORGETTABLE MOMENTS"
"MEET YOUR BABY BEFORE BIRTH"
Under headline:
4D Ultrasound • Early Gender • Pregnancy Confirmation
Business Name:
4D Little Lumen
Private Prenatal Ultrasound Studio
Phone Number:
850-471-5923
Important
This billboard must be readable in 5–6 seconds from a moving vehicle.
Less text is better.
The phone number and business name must be visible from a distance.
The design should feel like a premium brand that immediately tells expecting parents:
“This is where I go to see my baby.”
Files Provided
Official logo
Headshot
Ultrasound images
Don’t make this look like a medical office billboard.
Make it look like a luxury baby experience billboard. That’s what separates 4D Little Lumen from hospitals, OB offices, and all the new studios popping up around you. The emotional connection is what gets moms to book. ❤️
Billboard Size - 10.6” x 36”

```html
<!DOCTYPE html>
<html lang="en">
<head>
<meta charset="utf-8">
<title>4D Little Lumen Billboard</title>
<link rel="stylesheet" href="https://fonts.googleapis.com/css2?family=Michroma&display=swap">
<style>
  :root {
    --stage: #7a828a;
    --sage: #5a6863;
    --gold: #c99c36;
    --white: #ffffff;
    --paper: #f6f6f5;
    --clay: #b4644c;
    --clay-deep: #5a2418;
    --night: #1c1513;
  }
  html, body {
    margin: 0;
    padding: 0;
    width: 1145px;
    height: 1200px;
    overflow: hidden;
    background: var(--stage);
  }
  .billboard {
    position: absolute;
    left: 30px;
    top: 438px;
    width: 1085px;
    height: 324px;
    box-shadow: 0 8px 18px rgba(0,0,0,0.35);
  }
  .billboard svg {
    display: block;
    font-family: "Michroma", sans-serif;
  }
  .headline { fill: var(--sage); font-size: 54px; }
  .services { fill: var(--gold); font-size: 26px; }
  .phone { fill: var(--white); font-size: 46px; }
  .brand-name { fill: var(--gold); font-size: 15px; }
  .brand-tag { fill: var(--sage); font-size: 7.5px; letter-spacing: 0.5px; }
</style>
</head>
<body>
  <div class="billboard">
    <svg width="1085" height="324" viewBox="0 0 1085 324" xmlns="http://www.w3.org/2000/svg">
      <defs>
        <linearGradient id="headshot-tone" x1="0" y1="0" x2="0" y2="1">
          <stop offset="0" stop-color="#f1eee9"/>
          <stop offset="0.45" stop-color="#d8c4a0"/>
          <stop offset="1" stop-color="#3a3f3c"/>
        </linearGradient>
        <radialGradient id="scan-tone" cx="0.5" cy="0.45" r="0.6">
          <stop offset="0" stop-color="var(--clay)"/>
          <stop offset="0.7" stop-color="var(--clay-deep)"/>
          <stop offset="1" stop-color="var(--night)"/>
        </radialGradient>
        <linearGradient id="headshot-fade" x1="0" y1="0" x2="1" y2="0">
          <stop offset="0" stop-color="#ffffff" stop-opacity="0"/>
          <stop offset="1" stop-color="#f3f3f3"/>
        </linearGradient>
      </defs>

      <!-- base panel -->
      <rect class="panel" width="1085" height="324" fill="var(--white)"/>

      <!-- headshot area -->
      <rect x="0" y="0" width="192" height="270" fill="var(--paper)"/>
      <rect x="4" y="10" width="186" height="255" fill="url(#headshot-tone)"
            role="img" aria-label="Professional headshot of the studio owner"/>

      <!-- ultrasound image area -->
      <path d="M1085 0 L935 0 Q900 95 960 190 L1085 190 Z"
            fill="url(#scan-tone)" role="img" aria-label="4D ultrasound image of twin babies"/>
      <path d="M935 0 Q900 95 960 190" fill="none" stroke="var(--gold)" stroke-width="2"/>

      <!-- headline -->
      <text class="headline" x="540" y="68" text-anchor="middle" textLength="668" lengthAdjust="spacingAndGlyphs">MEET YOUR BABY</text>
      <text class="headline" x="540" y="124" text-anchor="middle" textLength="532" lengthAdjust="spacingAndGlyphs">BEFORE BIRTH</text>

      <!-- services -->
      <text class="services" x="568" y="161" text-anchor="middle" textLength="563" lengthAdjust="spacingAndGlyphs">4D Ultrasound • Early Gender</text>
      <text class="services" x="564" y="199" text-anchor="middle" textLength="479" lengthAdjust="spacingAndGlyphs">• Pregnancy Confirmation</text>

      <!-- lower band -->
      <path d="M0 262 Q560 232 1085 172 L1085 324 L0 324 Z" fill="var(--gold)"/>
      <path d="M0 275 Q560 245 1085 185 L1085 324 L0 324 Z" fill="var(--sage)"/>

      <!-- phone -->
      <g class="phone-icon">
        <circle cx="214" cy="297" r="18" fill="var(--gold)"/>
        <path d="M207 287 q-3 2 -2 6 q3 9 11 14 q4 2 6 -1 l2 -3 l-5 -3 l-2 2 q-5 -3 -7 -8 l2 -2 l-3 -5 z" fill="var(--night)"/>
      </g>
      <text class="phone" x="236" y="313" textLength="464" lengthAdjust="spacingAndGlyphs">850-471-5923</text>

      <!-- brand box -->
      <rect x="871" y="212" width="207" height="101" rx="12" fill="var(--white)"/>
      <text class="brand-name" x="974.5" y="265" text-anchor="middle" textLength="180" lengthAdjust="spacingAndGlyphs">4D Little Lumen</text>
      <line x1="890" y1="280" x2="1059" y2="280" stroke="var(--gold)" stroke-width="0.8"/>
      <text class="brand-tag" x="974.5" y="300" text-anchor="middle">PRENATAL ULTRASOUND STUDIO</text>
    </svg>
  </div>
</body>
</html>
```